Business Card Design

Consultation for design, construction athletic facilities specializing in synthetic turf systems and all weather running track systems.
Motto "True Owner Representation"
New Company that we'd like to highlight the LOGO first and foremost with the colors of the background and font as primary colors of the card too if possible. I've also attached a typical larger project design layout that could be used in the background to highlight our design and construction specialty.
Website is something we want very noticeable for driving traffic.
Target Market(s)
Athletic Directors, Designers, Government and Military, Contractors
Industry/Entity Type
Construction
Contact Information for Business Card
Peter L. Vandrell CFB, CTB
48317 W 63rd Ave
Harlow Ridge, WA 99482
C +1 503.555.0147
O +1 808.555.0182
Peter@fieldlaneco.example
www.fieldlaneco.example

```html
<!DOCTYPE html>
<html lang="en">
<head>
<meta charset="utf-8">
<title>Solvane Sport — Business Card</title>
<link rel="stylesheet" href="https://fonts.googleapis.com/css2?family=Cinzel:wght@400;600&family=Cormorant+SC:wght@500&display=swap">
<style>
  :root {
    --stage: #5e4a33;
    --card-black: #0b0b0b;
    --card-edge: #1d1d1d;
    --card-sheen: #2a2a2a;
    --gold: #e3b33a;
    --gold-soft: #c9982c;
    --ink-light: #cfcac2;
  }
  * { margin: 0; padding: 0; box-sizing: border-box; }
  html, body {
    width: 1200px; height: 795px; overflow: hidden;
    background: var(--stage);
  }
  .canvas {
    position: relative; width: 1200px; height: 795px;
    display: flex; align-items: center; justify-content: center; gap: 40px;
  }
  .card {
    position: relative; width: 540px; height: 309px;
    background: linear-gradient(160deg, var(--card-sheen) 0%, var(--card-black) 45%, var(--card-black) 100%);
    border: 1px solid var(--card-edge);
    border-radius: 4px;
    box-shadow: 0 14px 30px rgba(0,0,0,.45);
    overflow: hidden;
  }

  /* Front: contact side */
  .contact-block {
    position: absolute; left: 34px; bottom: 30px;
    color: var(--ink-light);
  }
  .person-name {
    font-family: "Cinzel", serif; font-weight: 600;
    font-size: 22px; letter-spacing: .04em; color: var(--gold);
    line-height: 1.1;
  }
  .person-credentials {
    font-family: "Cinzel", serif; font-weight: 600;
    font-size: 18px; letter-spacing: .05em; color: var(--gold);
    margin-bottom: 14px;
  }
  .detail-line {
    font-family: "Cormorant SC", serif; font-weight: 500;
    font-size: 14px; letter-spacing: .06em; line-height: 1.4;
  }
  .detail-gap { margin-top: 8px; }
  .detail-label { color: var(--gold); margin-right: 6px; }

  /* Back: brand side */
  .brand-lockup {
    position: absolute; inset: 0;
    display: flex; align-items: center; justify-content: center; gap: 16px;
  }
  .brand-mark { width: 26px; height: 26px; }
  .brand-name {
    font-family: "Cinzel", serif; font-weight: 400;
    font-size: 34px; letter-spacing: .22em; color: var(--gold-soft);
  }
</style>
</head>
<body>
<main class="canvas">

  <section class="card card--contact" aria-label="Business card, contact side">
    <div class="contact-block">
      <p class="person-name">Peter L. Vandrell</p>
      <p class="person-credentials">CFB, CTB</p>
      <p class="detail-line">48317 W 63rd Ave Harlow Ridge</p>
      <p class="detail-line">WA 99482</p>
      <p class="detail-line detail-gap"><span class="detail-label">C:</span>+1 503.555.0147</p>
      <p class="detail-line"><span class="detail-label">P:</span>+1 808.555.0182</p>
      <p class="detail-line">Peter@fieldlaneco.example</p>
      <p class="detail-line">www.fieldlaneco.example</p>
    </div>
  </section>

  <section class="card card--brand" aria-label="Business card, brand side">
    <div class="brand-lockup">
      <svg class="brand-mark" viewBox="0 0 26 26" aria-hidden="true">
        <circle cx="13" cy="13" r="12" fill="var(--gold-soft)"/>
      </svg>
      <p class="brand-name">SOLVANE SPORT</p>
    </div>
  </section>

</main>
</body>
</html>
```